K&T Holdings

Design a modern simple business card. I have attached a clean version of a card we like form Marrowfield Partners another company we own. I also attached the old K&T card design and logo and a couple of ideas we had but just can't finalize on whether we like them or not. We would like to include the 20 year logo somewhere on the card.

```html
<!DOCTYPE html>
<html lang="en">
<head>
<meta charset="utf-8">
<title>K&amp;T Holdings – Business Card</title>
<link href="https://fonts.googleapis.com/css2?family=Poppins:wght@300;400;500;700&display=swap" rel="stylesheet">
<style>
  :root {
    --navy: #27246b;
    --grey: #8c8c8c;
    --ink: #333338;
    --paper: #ffffff;
    --backdrop: #e9eeee;
    --rule: #b9b9c9;
  }
  * { box-sizing: border-box; margin: 0; padding: 0; }
  html, body {
    width: 1200px; height: 1200px; overflow: hidden;
    background: var(--backdrop);
    font-family: "Poppins", sans-serif;
    color: var(--ink);
  }
  .sheet {
    position: relative; width: 1200px; height: 1200px;
    display: flex; flex-direction: column; align-items: center; justify-content: center; gap: 80px;
  }
  .card {
    position: relative; width: 560px; height: 320px;
    background: var(--paper);
    box-shadow: 0 2px 8px rgba(0,0,0,0.08);
  }

  /* Front */
  .front-brand {
    position: absolute; top: 70px; left: 0; right: 0;
    display: flex; justify-content: center; align-items: center; gap: 26px;
  }
  .wordmark {
    font-weight: 700; color: var(--navy); letter-spacing: 1px;
    display: flex; align-items: center; gap: 10px;
  }
  .wordmark .dot { width: 14px; height: 14px; border-radius: 50%; background: var(--navy); }
  .front-brand .wordmark { font-size: 52px; }
  .brand-divider { width: 1px; height: 104px; background: var(--navy); }
  .anniversary { color: var(--navy); font-weight: 500; line-height: 1; }
  .anniversary .big { font-size: 40px; display: block; }
  .anniversary .span { font-size: 15px; letter-spacing: 2px; display: block; margin-top: 6px; }
  .tagline {
    position: absolute; top: 224px; left: 50%; transform: translateX(-50%);
    background: var(--navy); color: #fff; border-radius: 5px;
    font-size: 15px; font-weight: 400; padding: 6px 13px; white-space: nowrap;
  }
  .services {
    position: absolute; top: 280px; left: 0; right: 0;
    display: flex; justify-content: center; align-items: center;
    font-size: 12px; color: var(--ink); white-space: nowrap;
  }
  .services span + span { border-left: 1px solid var(--rule); margin-left: 10px; padding-left: 10px; }

  /* Back */
  .back .wordmark { position: absolute; top: 50px; right: 52px; font-size: 56px; }
  .person { position: absolute; left: 36px; top: 137px; }
  .person .name { font-size: 21px; color: var(--navy); font-weight: 400; letter-spacing: 0.3px; }
  .person .name b { font-weight: 700; }
  .person .role { font-size: 13.5px; font-weight: 300; margin-top: 6px; }
  .back-rule { position: absolute; left: 0; right: 0; top: 208px; height: 1px; background: var(--navy); opacity: .6; }
  .address {
    position: absolute; left: 36px; top: 226px; width: 170px;
    text-align: center; font-size: 13.5px; font-weight: 300; line-height: 1.4;
  }
  .address svg { display: block; margin: 0 auto 10px; }
  .contact { position: absolute; left: 320px; top: 226px; font-size: 15px; font-weight: 300; }
  .contact .row { display: flex; align-items: flex-start; gap: 10px; line-height: 1.55; }
  .contact svg { flex: none; margin-top: 2px; }
</style>
</head>
<body>
<main class="sheet">

  <section class="card front" aria-label="Card front">
    <div class="front-brand">
      <div class="wordmark"><span class="dot"></span>K&amp;T</div>
      <div class="brand-divider"></div>
      <div class="anniversary"><span class="big">20 Years</span><span class="span">2004-2024</span></div>
    </div>
    <div class="tagline">Integrated Industrial Services</div>
    <div class="services">
      <span>Mechanical/civil</span><span>I&amp;E</span><span>Fabrication</span><span>Rotating</span><span>Heat Transfer Equipment</span>
    </div>
  </section>

  <section class="card back" aria-label="Card back">
    <div class="wordmark"><span class="dot"></span>K&amp;T</div>
    <div class="person">
      <p class="name"><b>DANA</b> WHITFIELD</p>
      <p class="role">IT DIRECTOR</p>
    </div>
    <div class="back-rule"></div>
    <div class="address">
      <svg width="24" height="24" viewBox="0 0 24 24" aria-hidden="true">
        <circle cx="12" cy="12" r="12" fill="var(--navy)"/>
        <path d="M12 5.5a4.2 4.2 0 0 0-4.2 4.2c0 3.1 4.2 8 4.2 8s4.2-4.9 4.2-8A4.2 4.2 0 0 0 12 5.5z" fill="#fff"/>
        <circle cx="12" cy="9.7" r="1.6" fill="var(--navy)"/>
      </svg>
      48 Cedar street, Suite 410<br>Lakeport, TX 77590
    </div>
    <div class="contact">
      <div class="row">
        <svg width="22" height="22" viewBox="0 0 24 24" aria-hidden="true">
          <circle cx="12" cy="12" r="12" fill="var(--navy)"/>
          <path d="M8.3 6.2l1.8-.3 1.1 2.7-1.3 1a7 7 0 0 0 3.5 3.5l1-1.3 2.7 1.1-.3 1.8c-.2.7-.8 1.1-1.5 1.1A8.9 8.9 0 0 1 7.2 7.7c0-.7.4-1.3 1.1-1.5z" fill="#fff"/>
        </svg>
        <div>555-214-3307<br>555-214-3390</div>
      </div>
      <div class="row">
        <svg width="22" height="22" viewBox="0 0 24 24" aria-hidden="true">
          <circle cx="12" cy="12" r="12" fill="var(--navy)"/>
          <rect x="6.5" y="8" width="11" height="8" rx="1" fill="none" stroke="#fff" stroke-width="1.4"/>
          <path d="M6.8 8.4L12 12.5l5.2-4.1" fill="none" stroke="#fff" stroke-width="1.4"/>
        </svg>
        <div>dwhitfield@ktholdings.net</div>
      </div>
    </div>
  </section>

</main>
</body>
</html>
```